Lullio.com re-design on Wix platform

Re-do this website : www.lullio.com
Lullio is a sound conditioner that uses the calming, sedative qualities of mundane rhythmic stimulation to allow its users to rest easier and deeper than they normally would.
I think of Lullio.com as a web app; a place to use and buy the product. Im open to suggestion on site layouts, whether you use one page or several.
Use the same color scheme: purple, white, black, grey/silver
I would like a place for testimonials, even though you don't currently see one on the site. Other than that, assume the content will stay mostly the same.
I'd like a clean, modern, professional look. The site will reside on Wix platform.

```html
<!DOCTYPE html>
<html lang="en">
<head>
<meta charset="utf-8">
<title>Lullio</title>
<link href="https://fonts.googleapis.com/css2?family=Open+Sans:ital,wght@0,400;0,600;1,400&family=Roboto:wght@400;500&family=Roboto+Condensed:wght@400;700&display=swap" rel="stylesheet">
<style>
:root{
  --purple:#c21bd6;
  --purple-soft:#d94ee8;
  --ink:#222;
  --grey-text:#555;
  --light:#f5f5f6;
  --footer:#1b1b1b;
  --white:#fff;
}
*{margin:0;padding:0;box-sizing:border-box}
html,body{width:926px;height:1200px;overflow:hidden;background:var(--white)}
body{position:relative;font-family:"Open Sans",sans-serif;color:var(--ink)}
.abs{position:absolute}

/* header */
.site-header{position:absolute;left:0;top:0;width:926px;height:79px;background:var(--white);border-bottom:1px solid #e5e5e5}
.brand{position:absolute;left:76px;top:22px;display:flex;align-items:center;gap:8px;font-family:"Roboto",sans-serif;font-weight:500;font-size:36px;color:var(--ink);letter-spacing:1px}
.brand-mark{width:12px;height:12px;background:var(--purple)}
.main-nav{position:absolute;left:448px;top:32px;display:flex;gap:22px;font-family:"Roboto",sans-serif;font-size:10.5px;letter-spacing:.4px;color:#333}
.main-nav .active{color:var(--purple);position:relative}
.main-nav .active::after{content:"";position:absolute;left:0;right:0;top:45px;height:2px;background:var(--purple)}
.sound-btn{position:absolute;left:761px;top:27px;width:22px;height:22px;border:1px solid #333;border-radius:50%}
.share-btn{position:absolute;left:791px;top:27px;width:59px;height:22px;background:#3b5998;border-radius:2px;color:var(--white);font-family:"Roboto",sans-serif;font-weight:500;font-size:11px;display:flex;align-items:center;gap:5px;padding-left:5px}
.share-btn span.sq{width:12px;height:12px;background:var(--white)}

/* hero */
.hero{position:absolute;left:0;top:79px;width:926px;height:400px;background:linear-gradient(100deg,#3b3056 0%,#6a5a86 30%,#8a7f9e 50%,#4b4f86 75%,#2f3a72 100%)}
.hero-title{position:absolute;left:580px;top:326px;font-family:"Roboto Condensed",sans-serif;font-weight:700;font-size:39px;line-height:35px;color:var(--white)}
.hero-dots{position:absolute;left:580px;top:412px;display:flex;gap:7px;align-items:center}
.hero-dots i{display:block;width:8px;height:8px;border-radius:50%;background:var(--white)}
.hero-dots i.on{width:14px;height:14px;border:2px solid var(--white);background:transparent;position:relative}
.hero-dots i.on::after{content:"";position:absolute;left:2px;top:2px;width:6px;height:6px;border-radius:50%;background:var(--white)}

/* feature tiles */
.tile{position:absolute;top:501px;width:244px;height:176px}
.tile-label{position:absolute;left:47px;top:70px;width:150px;height:37px;background:var(--purple);border:2px solid rgba(255,255,255,.8);color:var(--white);font-family:"Roboto Condensed",sans-serif;font-size:16px;display:flex;align-items:center;justify-content:center}

/* testimonials */
.testimonials{position:absolute;left:0;top:700px;width:926px;height:226px;background:var(--light);border-top:1px solid #e8e8e8}
.section-title{position:absolute;left:76px;top:43px;font-family:"Roboto Condensed",sans-serif;font-size:20px;color:#333}
.quote{position:absolute;left:76px;top:78px;width:490px;font-style:italic;font-size:9.5px;line-height:16.5px;color:var(--grey-text)}
.author{position:absolute;left:76px;top:142px;font-size:12px;font-style:italic;color:#555}
.author em{color:var(--purple)}
.slider-bars{position:absolute;left:75px;top:177px;display:flex;gap:3px}
.slider-bars i{width:18px;height:2px;background:#ddd}
.slider-bars i.on{background:var(--purple)}
.offer{position:absolute;left:637px;top:720px;width:190px;height:190px;border:4px solid var(--purple-soft);border-radius:50%;background:#f1f1f1;text-align:center}
.offer-title{margin-top:28px;font-family:"Roboto Condensed",sans-serif;font-size:22px;line-height:25px;color:#333}
.offer-btn{display:inline-block;margin-top:10px;background:var(--purple);color:var(--white);font-family:"Roboto Condensed",sans-serif;font-size:12px;padding:6px 13px;border-radius:14px}
.offer-price{margin-top:6px;font-family:"Roboto Condensed",sans-serif;font-style:italic;font-size:18px;color:var(--purple)}

/* footer */
.site-footer{position:absolute;left:0;top:926px;width:926px;height:274px;background:var(--footer);color:var(--white)}
.footer-brand{position:absolute;left:76px;top:38px;display:flex;align-items:center;gap:8px;font-family:"Roboto",sans-serif;font-weight:500;font-size:36px;color:var(--white);letter-spacing:1px}
.contact-list{position:absolute;left:76px;top:99px;font-size:10px;line-height:15px;letter-spacing:.3px}
.contact-list li{list-style:none;display:flex;gap:12px;margin-bottom:11px}
.contact-list svg{flex:none}
.col-title{position:absolute;top:40px;font-family:"Roboto Condensed",sans-serif;font-size:14px}
.signup-text{position:absolute;left:316px;top:69px;width:230px;font-size:8.5px;line-height:14.5px}
.name-field{position:absolute;left:316px;top:108px;width:221px;height:32px;background:var(--white);color:#666;font-size:8.5px;padding:10px 11px}
.subscribe{position:absolute;left:316px;top:148px;width:77px;height:32px;background:var(--purple);font-family:"Roboto",sans-serif;font-weight:500;font-size:9.5px;display:flex;align-items:center;justify-content:center}
.quick-links{position:absolute;left:607px;top:68px;list-style:none;font-size:9.5px;line-height:18.5px}
.social-links{position:absolute;left:772px;top:70px;list-style:none;font-size:12px}
.social-links li{display:flex;align-items:center;gap:8px;height:28px}
.social-links i{width:20px;height:20px;border:1px solid #ccc;border-radius:50%}
.copyright{position:absolute;left:0;top:254px;width:926px;text-align:center;font-size:8.5px}
</style>
</head>
<body>

<header class="site-header">
  <div class="brand"><span class="brand-mark"></span>Lullio</div>
  <nav class="main-nav">
    <span class="active">HOME</span><span>ABOUT US</span><span>DOWNLOAD</span><span>BLOG</span><span>CONTACT</span>
  </nav>
  <div class="sound-btn">
    <svg width="20" height="20" viewBox="0 0 20 20"><path d="M5 8h3l3-3v10l-3-3H5z" fill="none" stroke="#333" stroke-width="1"/><path d="M13 7.5q2 2.5 0 5" fill="none" stroke="#333"/></svg>
  </div>
  <div class="share-btn"><span class="sq"></span>Share</div>
</header>

<section class="hero" role="img" aria-label="Child sleeping peacefully in bed by a window with potted plants at dusk">
  <h1 class="hero-title">TRICKS TO JUMP<br>INTO SLEEP</h1>
  <div class="hero-dots"><i class="on"></i><i></i><i></i><i></i></div>
</section>

<div class="tile" style="left:76px;background:linear-gradient(160deg,#3a4a6e,#5b6a8c 50%,#2c3450)" role="img" aria-label="Audio mixing console">
  <div class="tile-label">INSTRUCTIONS</div>
</div>
<div class="tile" style="left:341px;background:linear-gradient(120deg,#cfc6bb,#a89f94 55%,#3a2a1e)" role="img" aria-label="Sheet music resting on piano keys">
  <div class="tile-label">HOW IT WORKS</div>
</div>
<div class="tile" style="left:606px;background:linear-gradient(160deg,#d8d6d4,#b9b7b6 50%,#3c5a86)" role="img" aria-label="Person resting on a sofa wearing headphones">
  <div class="tile-label">WHAT TO EXPECT</div>
</div>

<section class="testimonials">
  <h2 class="section-title">TESTIMONIALS</h2>
  <p class="quote">“ Lorem ipsum dolor sit amet, consectetur adipiscing elit, sed do eiusmod tempor incididunt ut labore et dolore magna aliqua. Ut enim ad minim veniam, quis nostrud exercitation ullamco laboris nisi ut aliquip ex ea commodo consequat. Duis aute irure dolor in reprehenderit in voluptate velit esse cillum dolore eu fugiat nulla pariatur.</p>
  <p class="author"><em>John Doe</em> - Lullio</p>
  <div class="slider-bars"><i class="on"></i><i></i><i></i></div>
</section>

<aside class="offer">
  <div class="offer-title">WANT TO OWN<br>10 CONTINUOUS<br>HOURS ?</div>
  <div class="offer-btn">DOWNLOAD NOW!</div>
  <div class="offer-price">$2.99</div>
</aside>

<footer class="site-footer">
  <div class="footer-brand"><span class="brand-mark"></span>Lullio</div>
  <ul class="contact-list">
    <li><svg width="14" height="16" viewBox="0 0 14 16"><path d="M7 15s5-5.5 5-9A5 5 0 0 0 2 6c0 3.5 5 9 5 9z" fill="none" stroke="#fff"/><circle cx="7" cy="6" r="1.8" fill="none" stroke="#fff"/></svg><span>LULLIO 120<br>Harbor Avenue 204518</span></li>
    <li><svg width="14" height="14" viewBox="0 0 14 14"><path d="M2 1.5l3 .5 1 3-1.5 1.2a8 8 0 0 0 4 4L10 8.5l3 1 .5 3C8 13 1 6 2 1.5z" fill="none" stroke="#fff"/></svg><span>Phone : &nbsp;555 0142 7000</span></li>
    <li><svg width="14" height="12" viewBox="0 0 14 12"><rect x=".5" y="1.5" width="13" height="9" fill="none" stroke="#fff"/><path d="M.5 1.5l6.5 5 6.5-5" fill="none" stroke="#fff"/></svg><span>E-mail: info@lullio.com</span></li>
  </ul>

  <h3 class="col-title" style="left:316px">SIGN UP TO RECEIVE EMAIL</h3>
  <p class="signup-text">Excepteur sint occaecat cupidatat non proident, sunt in culpa qui Nemo enim ipsam voluptatem</p>
  <div class="name-field">Enter Name</div>
  <div class="subscribe">SUBSCRIBE</div>

  <h3 class="col-title" style="left:607px">QUICK LINKS</h3>
  <ul class="quick-links">
    <li>Home</li><li>About Us</li><li>How It Works</li><li>Tricks To Jump Into Sleep</li><li>Other Tips For Great Sleep</li><li>Contact Us</li>
  </ul>

  <h3 class="col-title" style="left:772px">SOCIAL MEDIA</h3>
  <ul class="social-links">
    <li><i></i>Friendbook</li><li><i></i>Chirper</li><li><i></i>Circles</li><li><i></i>Tubecast</li>
  </ul>

  <p class="copyright">Copyright © LULLIO 2017. All rights reserved.</p>
</footer>

</body>
</html>
```